Flyer-Design für Tierphysiotherapie und Osteopathie
Zielgruppe
Tierphysiotherapie und Osteopathie Lotte Brenner
Aufgabenstellung
Text des gewünschten Flyers ist hochgeladen.
Ebenso die Visitenkarten und das Logo, sowie die Website - zur Orientierung von Farben, Schriftarten, etc.
Auch ein paar Bilder sind beigefügt.

```html
<!DOCTYPE html>
<html lang="de">
<head>
<meta charset="utf-8">
<title>Lotte Brenner – Tierphysiotherapie &amp; Osteopathie Flyer</title>
<link href="https://fonts.googleapis.com/css2?family=Bebas+Neue&family=Source+Sans+3:wght@300;400;600&display=swap" rel="stylesheet">
<style>
:root{
  --stage:#c5c1bf;
  --paper:#ffffff;
  --taupe:#766c68;
  --amber:#f0b22e;
  --cream:#f9dba1;
  --stone:#d6d0ce;
  --ink:#6e6562;
  --white:#ffffff;
}
*{margin:0;padding:0;box-sizing:border-box}
html,body{width:1200px;height:567px;overflow:hidden;background:var(--stage)}
body{font-family:"Source Sans 3",sans-serif;font-weight:300;position:relative}
.page{position:absolute;top:22px;width:523px;height:523px;background:var(--paper)}
.page--front{left:65px}
.page--back{left:612px}
.grid{position:absolute;left:14px;top:14px;width:493px;height:496px;display:grid;grid-template-columns:248px 245px;grid-template-rows:247px 249px}
.cell{position:relative;overflow:hidden}
.cell--taupe{background:var(--taupe)}
.cell--amber{background:var(--amber)}
.cell--cream{background:var(--cream)}
.cell--stone{background:var(--stone)}
.photo--horse{background:linear-gradient(120deg,#5a3a2a 0%,#6b4632 40%,#4ea8b3 75%,#7d6a5a 100%)}
.photo--dog{background:linear-gradient(160deg,#9fb07a 0%,#b597c9 35%,#5a7a3e 70%,#3d2a22 100%)}

.brand{position:absolute;left:0;right:0;top:108px;text-align:center;color:var(--white);font-size:24px;font-weight:300;letter-spacing:.5px}
.brand__dot{display:inline-block;width:12px;height:12px;border-radius:50%;background:var(--amber);margin-right:8px;vertical-align:middle}

.card{position:absolute;left:25px;top:85px;color:var(--white)}
.card__name{font-family:"Bebas Neue",sans-serif;font-size:34px;font-weight:400;letter-spacing:2.5px;line-height:1}
.card__role{font-size:12px;letter-spacing:1.2px;margin-top:10px}
.contact{margin-top:16px;font-size:11.5px;letter-spacing:1.1px;line-height:19px;white-space:nowrap}
.contact__row{display:flex;align-items:center;gap:14px}
.contact__icon{width:13px;height:13px;flex:none}

.panel{position:absolute;left:22px;right:20px;top:14px;font-size:13px;line-height:16.3px;letter-spacing:.2px}
.intro{color:var(--amber);text-align:justify;hyphens:auto;-webkit-hyphens:auto;top:18px;left:23px;right:18px;letter-spacing:0}
.intro__title{font-weight:600;font-size:12.5px;line-height:16.5px;margin-bottom:9px;letter-spacing:-.3px;white-space:nowrap;text-align:left}
.intro p+p{margin-top:9px}
.wish{color:var(--ink);left:18px;top:12px}
.wish__title{font-weight:600;font-size:13px;margin-bottom:2px}
.list{list-style:none}
.list li{position:relative;padding-left:15px}
.list li::before{content:"•";position:absolute;left:0;font-size:9px}
.wish .list li{margin-bottom:9px}
.services{color:var(--ink);top:22px}
.services__claim{font-weight:600;font-size:13px;margin-top:10px;text-align:justify;letter-spacing:0}
.services__text{margin-top:9px;text-align:justify;hyphens:auto;-webkit-hyphens:auto}
.support{color:var(--white);left:20px;right:16px;top:22px}
.support__call{font-weight:600;margin-top:16px;font-size:13px;letter-spacing:0}
.support .contact{margin-top:16px}
</style>
</head>
<body>

<section class="page page--front">
  <div class="grid">
    <div class="cell cell--taupe">
      <div class="brand"><span class="brand__dot"></span>Lotte Brenner</div>
    </div>
    <div class="cell photo--horse" role="img" aria-label="Foto: Therapeutin im türkisen Shirt streichelt ein braunes Pferd vor einer Holzwand"></div>
    <div class="cell photo--dog" role="img" aria-label="Foto: Therapeutin kniet auf einer Wiese und behandelt einen braunen Hund"></div>
    <div class="cell cell--amber">
      <div class="card">
        <h1 class="card__name">Lotte Brenner</h1>
        <p class="card__role">Tierphysiotherapie &amp; Osteopathie</p>
        <div class="contact">
          <div class="contact__row"><svg class="contact__icon" viewBox="0 0 24 24"><path fill="#fff" d="M6.6 10.8a15 15 0 0 0 6.6 6.6l2.2-2.2c.3-.3.7-.4 1-.2 1.1.4 2.3.6 3.6.6.6 0 1 .4 1 1V20c0 .6-.4 1-1 1A17 17 0 0 1 3 4c0-.6.4-1 1-1h3.5c.6 0 1 .4 1 1 0 1.3.2 2.5.6 3.6.1.3 0 .7-.2 1z"/></svg>0170/3826415</div>
          <div class="contact__row"><svg class="contact__icon" viewBox="0 0 24 24"><path fill="#fff" d="M2 5h20v14H2z"/><path fill="none" stroke="#f0b22e" stroke-width="1.6" d="M2 5l10 8 10-8"/></svg>info@tierphysio-brenner.de</div>
        </div>
      </div>
    </div>
  </div>
</section>

<section class="page page--back">
  <div class="grid">
    <div class="cell cell--taupe">
      <div class="panel intro">
        <h2 class="intro__title">Ich heiße Lotte Brenner und bin Physio-<br>therapeutin und Osteopathin für Tiere</h2>
        <p>Einschränkungen, Blockaden oder Schmerzen können viele Ursachen haben und äußern sich bei jedem Tier anders. Ihr Tier ist einzigartig, deshalb bekommen Sie bei mir die Behand&shy;lung, die zu Ihrem Tier und Ihnen passt!</p>
        <p>Neben der Arbeit mit meinen Händen biete ich unter&shy;schiedliche Therapie&shy;formen und Leistungen an wie z.B.:</p>
      </div>
    </div>
    <div class="cell cell--cream">
      <div class="panel wish">
        <h2 class="wish__title">Sie möchten:</h2>
        <ul class="list">
          <li>Ihrem Jungtier einen guten Start ins Leben ermöglichen?</li>
          <li>Ihr Tier langfristig fit erhalten, um bis ins hohe Alter viel Spaß an gemeinsamen Unternehmun&shy;gen zu haben?</li>
          <li>Ihren Sportler professionell be gleiten lassen?</li>
          <li>Durch regelmäßigen CheckUp, frühzeitig handeln können, wenn doch mal was zwickt oder klemmt</li>
        </ul>
      </div>
    </div>
    <div class="cell cell--stone">
      <div class="panel services">
        <ul class="list">
          <li>Lasertherapie</li>
          <li>Neurostim</li>
          <li>aktives und passives Bewegungstraining</li>
          <li>gezielter Muskelaufbau</li>
          <li>und vieles mehr</li>
        </ul>
        <p class="services__claim">Ich gehe ganz besonders auf die spe&shy;ziellen Bedürfnisse Ihres Tiere ein.</p>
        <p class="services__text">Und begleite Sie und Ihr Tier liebevoll und einfühlsam. Gemeinsam finden wir den besten Weg zu mehr Bewe&shy;gung und Lebensfreude!</p>
      </div>
    </div>
    <div class="cell cell--amber">
      <div class="panel support">
        <ul class="list">
          <li>bei Beschwerden im Bewegungs&shy;apparat wie z.B. HD, ED, Band&shy;scheibenvorfällen oder neurolo&shy;gischen Einschränkungen, nach Verletzungen oder Operationen kompetent und mit viel Feinge&shy;fühl unterstützt werden?</li>
        </ul>
        <p class="support__call">Dann sind Sie bei mir genau Richtig!</p>
        <div class="contact">
          <div class="contact__row"><svg class="contact__icon" viewBox="0 0 24 24"><path fill="#fff" d="M6.6 10.8a15 15 0 0 0 6.6 6.6l2.2-2.2c.3-.3.7-.4 1-.2 1.1.4 2.3.6 3.6.6.6 0 1 .4 1 1V20c0 .6-.4 1-1 1A17 17 0 0 1 3 4c0-.6.4-1 1-1h3.5c.6 0 1 .4 1 1 0 1.3.2 2.5.6 3.6.1.3 0 .7-.2 1z"/></svg>0170/3826415</div>
          <div class="contact__row"><svg class="contact__icon" viewBox="0 0 24 24"><path fill="#fff" d="M2 5h20v14H2z"/><path fill="none" stroke="#f0b22e" stroke-width="1.6" d="M2 5l10 8 10-8"/></svg>info@tierphysio-brenner.de</div>
        </div>
      </div>
    </div>
  </div>
</section>

</body>
</html>
```